We have built a site at brightgadgetnotes.net, but it is missing several elements and several don't work. I even like the color scheme we have. I do not know to do too much with code so if there is anything I need to do, it must be very minimal.

We essentially want what is there with:

1) a small column on the left side for categories, which are currently bottom right
2) space for a 728-90 banner ad at the top under the menu below the logo
3) drop down menus under the top logo that actually work
4) the top menu (where we have ages), the logo, the drop down menus and the 728-90 banner all need to space together neatly
5) the top logo needs to center
6) under the title of each post on the home page it says "comment and reactions." I'd like reactions removed since I have no idea what they are.
7) must be able to accept all widgets
8) I need a simple way to access the code to the top banner ad when it is placed to change as needed

That's about it other than any suggestions to make it better. I like clean and simple in blog format.
Updates

Sorry I should have mentioned that we want the text of the categories smaller so that can fit in a smaller left column. I'd have to see but I'd guess about 10 point.

Industry/Entity Type

Work

Requirements
Must have
• see above

```html
<!DOCTYPE html>
<html lang="en">
<head>
<meta charset="utf-8">
<title>Bright Gadget Notes</title>
<link rel="stylesheet" href="https://fonts.googleapis.com/css2?family=Roboto+Condensed:wght@400;700&family=Source+Sans+3:wght@300;400;500;600;700&family=Open+Sans:wght@300;700&display=swap">
<style>
:root{
  --page-bg:#ebe8df;
  --topbar-bg:#f2f0ea;
  --dark:#3a3330;
  --dark-2:#2a2421;
  --white:#ffffff;
  --text:#5a5450;
  --heading:#2b2522;
  --green:#6db413;
  --green-light:#8ed11e;
  --green-dark:#4f9a00;
  --sky:#a9dcf4;
  --sky-dark:#8ccbea;
  --line:#e4e1da;
  --meta-bg:#f0eeea;
  --muted:#8a847f;
}
*{box-sizing:border-box;margin:0;padding:0}
html,body{width:1200px;height:2261px;overflow:hidden}
body{background:var(--page-bg);font-family:"Source Sans 3",sans-serif;color:var(--text);position:relative}
a{color:inherit;text-decoration:none}
ul{list-style:none}

.age-bar{position:absolute;left:0;top:0;width:1200px;height:51px;background:var(--topbar-bg);box-shadow:0 1px 3px rgba(0,0,0,.08)}
.age-nav{position:absolute;right:39px;top:15px;font-family:"Roboto Condensed",sans-serif;font-size:15px;color:var(--heading);display:flex;gap:10px}
.age-nav .sep{color:var(--muted)}

.brand{position:absolute;left:0;width:1200px;top:94px;text-align:center;font-family:"Source Sans 3",sans-serif;font-weight:700;font-size:44px;color:var(--dark);letter-spacing:1px;display:flex;justify-content:center;align-items:center;gap:14px}
.brand-mark{width:26px;height:26px;border-radius:50%;background:var(--green)}

.page{position:absolute;left:62px;top:176px;width:1075px;height:1988px;background:var(--white)}

.main-nav{position:absolute;left:62px;top:176px;width:1075px;height:55px;background:linear-gradient(#4a423e,var(--dark-2));font-family:"Roboto Condensed",sans-serif;font-weight:700;font-size:18px;color:var(--white);z-index:3}
.main-nav .item{position:absolute;top:0;height:55px;line-height:55px;padding:0 20px;border-right:1px solid #5b524d}
.main-nav .item.active{background:var(--dark-2)}
.search{position:absolute;left:800px;top:12px;width:255px;height:32px;background:var(--white);border-radius:3px;font-family:"Source Sans 3",sans-serif;font-style:italic;font-weight:400;font-size:14px;color:var(--muted);padding:7px 12px}
.search svg{position:absolute;right:9px;top:8px}
.dropdown{position:absolute;left:356px;top:231px;width:188px;background:var(--dark-2);padding:6px 0 8px;z-index:4;font-size:14px;color:#e8e4e0}
.dropdown li{margin:0 21px 0 20px;padding:7px 2px 8px;border-bottom:1px solid #4a423e}
.dropdown li:last-child{border-bottom:none}

.leaderboard{position:absolute;left:216px;top:244px;width:764px;height:95px;background:linear-gradient(90deg,#8fd0ef,#d8eef7 45%,#9fd1ea)}

.hero{position:absolute;left:87px;top:354px;width:1027px;height:364px;background:var(--sky);border:1px solid var(--sky-dark);border-radius:3px;overflow:hidden}
.hero-copy{position:absolute;left:58px;top:94px;width:390px;z-index:2}
.hero-kicker{font-family:"Open Sans",sans-serif;font-weight:300;font-size:29px;line-height:34px;color:var(--heading);white-space:nowrap}
.hero-title{font-family:"Open Sans",sans-serif;font-weight:700;font-size:38px;line-height:46px;color:var(--heading);white-space:nowrap}
.hero-text{margin-top:4px;width:375px;font-size:15px;line-height:19px;color:#3e4a52}
.hero-dots{margin-top:14px;display:flex;gap:3px}
.hero-dots span{width:11px;height:11px;border-radius:50%;background:#6d7b84}
.hero-dots span:first-child{background:#3c4950}
.hero-art{position:absolute;left:480px;top:58px;width:480px;height:255px;border-radius:14px;background:linear-gradient(180deg,#bfe6f7,#eef7fb 60%,#d3ecd0)}

.sidebar{position:absolute;left:86px;width:303px}
.widget{background:var(--white);border:1px solid var(--line);border-radius:3px}
.categories{top:739px;height:555px}
.widget-head-green{height:50px;background:linear-gradient(var(--green-light),var(--green-dark));color:var(--white);font-family:"Roboto Condensed",sans-serif;font-weight:700;font-size:20px;padding:13px 33px}
.cat-list{padding:13px 0 0 33px;font-size:14px;color:#5c5652}
.cat-list li{height:29.4px;position:relative;padding-left:18px}
.cat-list li::before{content:"";position:absolute;left:0;top:6px;border-left:5px solid #555;border-top:4px solid transparent;border-bottom:4px solid transparent}
.scroll-track{position:absolute;left:265px;top:68px;width:10px;height:464px;background:#e8e5dc;border-radius:4px}
.scroll-thumb{position:absolute;left:262px;top:125px;width:16px;height:79px;background:var(--dark-2);border-radius:3px}

.alert{top:1309px;height:158px;padding:16px 26px}
.alert-title{font-family:"Roboto Condensed",sans-serif;font-weight:700;font-size:20px;color:var(--green)}
.alert-note{font-size:14px;color:var(--text);margin-top:4px}
.alert-input{margin-top:8px;width:253px;height:30px;background:#f3f1ec;font-size:14px;color:var(--muted);padding:5px 10px}
.alert-btn{position:absolute;right:24px;top:113px;width:82px;height:32px;background:var(--dark);color:var(--white);font-size:14px;text-align:center;line-height:32px;border-radius:2px}

.side-ad{top:1487px;height:255px;background:linear-gradient(180deg,#d8d8d8,#f4f4f4 40%,#eaeaea 85%,#f07a1c)}

.popular{top:1757px;height:316px}
.popular-head{height:53px;background:linear-gradient(#ffffff,#f1efea);border-bottom:1px solid var(--line);font-size:21px;color:var(--heading);padding:12px 32px}
.popular-list{padding:20px 0 0 34px;font-size:15px;color:#4a4440}
.popular-list li{width:188px;height:33px;padding:0 0 0 18px;border-bottom:1px solid #eeebe6;position:relative;line-height:26px}
.popular-list li::before{content:"";position:absolute;left:0;top:9px;border-left:5px solid #777;border-top:4px solid transparent;border-bottom:4px solid transparent}

.post{position:absolute;left:427px;width:687px}
.post-title{font-size:22px;font-weight:500;color:var(--heading);line-height:26px}
.post-body{font-size:14px;line-height:22.6px;color:var(--text);font-weight:400}
.post-thumb{position:absolute;left:1px;width:232px;height:112px}
.post-excerpt{position:absolute;left:249px;width:438px}
.post-meta{position:absolute;left:0;height:35px;width:440px;font-size:13px;color:#4a4440;display:flex;align-items:center}
.meta-strip{display:flex;align-items:center;gap:20px;background:var(--meta-bg);height:35px;padding:0 10px;border-radius:2px}
.meta-strip span{display:flex;align-items:center;gap:6px}
.more-btn{position:absolute;left:328px;top:0;width:114px;height:35px}
.more-btn span{position:absolute;left:0;top:0;width:114px;height:35px;line-height:35px;padding-left:17px;color:var(--white);font-size:14px;font-weight:600}
.post-rule{position:absolute;left:0;width:687px;height:6px;background:linear-gradient(90deg,rgba(0,0,0,0),rgba(0,0,0,.05) 50%,rgba(0,0,0,0))}

.pager{position:absolute;left:437px;top:2102px;display:flex;gap:9px;font-size:13px;font-weight:600;color:var(--white)}
.pager a{height:26px;line-height:26px;min-width:27px;padding:0 7px;text-align:center;background:#5a514c;border-radius:2px}
.pager a.wide{min-width:56px}

.footer{position:absolute;left:0;top:2164px;width:1200px;height:97px;background:var(--dark)}
.copyright{position:absolute;left:93px;top:36px;font-size:14px;color:#d9d4cf}
.social{position:absolute;left:995px;top:32px;display:flex;gap:7px}
.social span{width:24px;height:24px;border-radius:50%;background:var(--white)}
</style>
</head>
<body>

<header class="age-bar">
  <nav class="age-nav">
    <a>AGES 1-2 (TODDLER)</a><span class="sep">|</span>
    <a>AGES 3-4 (PRESCHOOL)</a><span class="sep">|</span>
    <a>AGES 5-6</a><span class="sep">|</span>
    <a>AGES 7-8</a><span class="sep">|</span>
    <a>AGES 9-10</a>
  </nav>
</header>

<div class="brand"><span class="brand-mark"></span>Bright Gadget Notes</div>

<div class="page"></div>

<nav class="main-nav">
  <a class="item" style="left:0">BEST FREE APPS</a>
  <a class="item" style="left:166px">FREE APPS</a>
  <a class="item active" style="left:294px">BEST APPS</a>
  <a class="item" style="left:418px;border-right:none">SUBMIT APP</a>
  <div class="search">Search here
    <svg width="16" height="16" viewBox="0 0 16 16"><circle cx="6.5" cy="6.5" r="5" fill="none" stroke="#333" stroke-width="2"/><line x1="10" y1="10" x2="15" y2="15" stroke="#333" stroke-width="2.4"/></svg>
  </div>
</nav>
<ul class="dropdown">
  <li>Maecenas aliquet</li>
  <li>Velit vel turpis</li>
  <li>Mauris neque metus</li>
  <li>Malesuada nec</li>
</ul>

<div class="leaderboard" role="img" aria-label="728 by 90 banner ad: a laptop among pencils and city towers"></div>

<section class="hero">
  <div class="hero-art" role="img" aria-label="Illustration of an ice cream van with small green robot mascots"></div>
  <div class="hero-copy">
    <div class="hero-kicker">PHASELLUS FELIS DOLOR</div>
    <div class="hero-title">BEST POCKETA APPS</div>
    <p class="hero-text">Mauris vel lacus vitae felis vestibulum volutpat. Etiam est nunc, venenatis in, tristique eu, imperdiet ac, nisl. Cum sociis natoque penatibus et magnis</p>
    <div class="hero-dots"><span></span><span></span><span></span><span></span></div>
  </div>
</section>

<aside>
  <div class="sidebar widget categories">
    <div class="widget-head-green">APP CATEGORY</div>
    <ul class="cat-list">
      <li>addition (2)</li>
      <li>ages 1-2 (toddler) (2)</li>
      <li>ages 3-4 (preschool) (9)</li>
      <li>ages 5-6 (7)</li>
      <li>ages 7-8 (2)</li>
      <li>ages 8-9 (1)</li>
      <li>ages 9-10 (2)</li>
      <li>alphabet/letters (3)</li>
      <li>animals (1)</li>
      <li>art (2)</li>
      <li>best apps (3)</li>
      <li>best free apps (2)</li>
      <li>books (1)</li>
      <li>coloring (1)</li>
      <li>colors (1)</li>
      <li>connect the dots (1)</li>
    </ul>
    <div class="scroll-track"></div>
    <div class="scroll-thumb"></div>
  </div>

  <div class="sidebar widget alert">
    <div class="alert-title">POCKETA APP ALERT</div>
    <div class="alert-note">Subscribe to our Pocketa Alert!</div>
    <div class="alert-input">email address</div>
    <div class="alert-btn">Sing Up</div>
  </div>

  <div class="sidebar side-ad" role="img" aria-label="Trendmart fashion ad with watches and shirts, 30 days free returns"></div>

  <div class="sidebar widget popular">
    <div class="popular-head">Most Popular Posts</div>
    <ul class="popular-list">
      <li>Duis sed tellus et</li>
      <li>Rortor vestibulum gravida</li>
      <li>Praesent elementum</li>
      <li>Elit at tellus</li>
      <li>Curabitur metus ipsum</li>
      <li>Luctus eu malesuada ut</li>
    </ul>
  </div>
</aside>

<svg width="0" height="0" style="position:absolute">
  <defs>
    <symbol id="icon-clock" viewBox="0 0 16 16"><circle cx="8" cy="8" r="6.5" fill="none" stroke="#333" stroke-width="2"/><path d="M8 4v4h3" fill="none" stroke="#333" stroke-width="1.8"/></symbol>
    <symbol id="icon-user" viewBox="0 0 16 16"><circle cx="8" cy="5" r="3.5" fill="#333"/><path d="M1 16c0-5 3-7 7-7s7 2 7 7z" fill="#333"/></symbol>
    <symbol id="icon-comment" viewBox="0 0 18 14"><ellipse cx="9" cy="6" rx="8.5" ry="5.5" fill="#333"/><path d="M3 9l-2 5 6-3z" fill="#333"/></symbol>
    <symbol id="btn-more" viewBox="0 0 114 35"><defs><linearGradient id="g-more" x1="0" y1="0" x2="0" y2="1"><stop offset="0" stop-color="#8ed11e"/><stop offset="1" stop-color="#4f9a00"/></linearGradient></defs><path d="M0 0h100l14 17.5L100 35H0z" fill="url(#g-more)"/></symbol>
  </defs>
</svg>

<article class="post" style="top:750px">
  <h2 class="post-title">We’re still under Construction!</h2>
  <p class="post-body" style="margin-top:6px">Welcome! Have a look around but we’re still under construction! We’ll have a full launch soon!<br>In the meantime, please subscribe to one of our social media options in the right column to be notified when the site is finished.<br>Thanks!</p>
  <div class="post-meta" style="top:140px">
    <div class="meta-strip"><span><svg width="16" height="16"><use href="#icon-clock"/></svg>APRIL 12, 2013</span><span><svg width="16" height="16"><use href="#icon-user"/></svg>Admin</span><span><svg width="18" height="14"><use href="#icon-comment"/></svg>Comments</span></div>
    <a class="more-btn"><svg width="114" height="35"><use href="#btn-more"/></svg><span>Learn More</span></a>
  </div>
  <div class="post-rule" style="top:204px"></div>
</article>

<article class="post" style="top:988px">
  <h2 class="post-title">Dr. Pebble’s Beauty Salon (best apps)</h2>
  <div class="post-thumb" style="top:43px;background:linear-gradient(135deg,#f2a4c8,#c9e6f5)" role="img" aria-label="Screenshot of a cartoon beauty salon game"></div>
  <p class="post-body post-excerpt" style="top:40px">Tinkerhop has released another app that’s part of their excellent Dr. Pebble series. In Dr. Pebble’s Beauty Salon, children can paint cow fin-gernails, pluck sheep nose hairs and even put lipstick on a pig! The app is just $1.99 for launch. The Dr. Pebble’s are all very good and if a beauty salon won’t be your child’s thing they also have a restaurant,</p>
  <div class="post-meta" style="top:179px">
    <div class="meta-strip"><span><svg width="16" height="16"><use href="#icon-clock"/></svg>APRIL 12, 2013</span><span><svg width="16" height="16"><use href="#icon-user"/></svg>Admin</span><span><svg width="18" height="14"><use href="#icon-comment"/></svg>Comments</span></div>
    <a class="more-btn"><svg width="114" height="35"><use href="#btn-more"/></svg><span>Learn More</span></a>
  </div>
  <div class="post-rule" style="top:247px"></div>
</article>

<article class="post" style="top:1270px">
  <h2 class="post-title">Kite Kids Super Whiz ABC Adventures</h2>
  <div class="post-thumb" style="top:43px;background:linear-gradient(135deg,#e9c03a,#3f7fc4)" role="img" aria-label="Cover art of an alphabet adventure game"></div>
  <p class="post-body post-excerpt" style="top:40px">Super Whiz ABC Adventures ($3.99) is one of the top selling paid educational Pocketa apps at the time of this writing. It’s a terrific app based on the Kite Kids show Super Whiz, with five different games and four videos covering the ABCs. There are very few apps as good as this on Pocketa</p>
  <div class="post-meta" style="top:179px">
    <div class="meta-strip"><span><svg width="16" height="16"><use href="#icon-clock"/></svg>APRIL 12, 2013</span><span><svg width="16" height="16"><use href="#icon-user"/></svg>Admin</span><span><svg width="18" height="14"><use href="#icon-comment"/></svg>Comments</span></div>
    <a class="more-btn"><svg width="114" height="35"><use href="#btn-more"/></svg><span>Learn More</span></a>
  </div>
  <div class="post-rule" style="top:247px"></div>
</article>

<article class="post" style="top:1552px">
  <h2 class="post-title">The Thimblewick (best apps)</h2>
  <div class="post-thumb" style="top:43px;left:4px;background:linear-gradient(135deg,#7ccbe8,#f3e27a)" role="img" aria-label="Cover art of a picture storybook app"></div>
  <p class="post-body post-excerpt" style="top:40px">Unless someone like you cares a whole awful lot, nothing is going to get better. It’s not.”<br>Not a free app this time, but one well worth the cost. Harborlight Media produces the Dr. Quillby apps for Pocketa, SlateTab and PocketPhone and they are terrific.</p>
  <div class="post-meta" style="top:179px;left:4px">
    <div class="meta-strip"><span><svg width="16" height="16"><use href="#icon-clock"/></svg>APRIL 12, 2013</span><span><svg width="16" height="16"><use href="#icon-user"/></svg>Admin</span><span><svg width="18" height="14"><use href="#icon-comment"/></svg>Comments</span></div>
    <a class="more-btn"><svg width="114" height="35"><use href="#btn-more"/></svg><span>Learn More</span></a>
  </div>
  <div class="post-rule" style="top:247px"></div>
</article>

<article class="post" style="top:1833px">
  <h2 class="post-title">Puzzlewink Kids Puzzles (best free apps)</h2>
  <div class="post-thumb" style="top:43px;left:6px;background:linear-gradient(135deg,#c8202a,#f0d6c0)" role="img" aria-label="Title screen of a kids puzzle app with a play button"></div>
  <p class="post-body post-excerpt" style="top:40px;left:253px;width:434px">We named Puzzlewink a Top Pick on brightkidnotes.net because it’s an extremely well-done, provides several puzzles free and is a different kind of puzzle app for preschoolers. Keep in mind there are several versions of Puzzlewink. The Play Lane and Riverbox versions are free with in-app purchases.</p>
  <div class="post-meta" style="top:179px;left:4px">
    <div class="meta-strip"><span><svg width="16" height="16"><use href="#icon-clock"/></svg>APRIL 12, 2013</span><span><svg width="16" height="16"><use href="#icon-user"/></svg>Admin</span><span><svg width="18" height="14"><use href="#icon-comment"/></svg>Comments</span></div>
    <a class="more-btn"><svg width="114" height="35"><use href="#btn-more"/></svg><span>Learn More</span></a>
  </div>
</article>

<nav class="pager">
  <a class="wide">Prev</a><a>1</a><a>2</a><a>3</a><a>4</a><a>5</a><a>6</a><a>…</a><a>22</a><a class="wide">Next</a>
</nav>

<footer class="footer">
  <div class="copyright">© 2013 Bright Gadget Notes. All Rights Reserved.&nbsp; Term of Use</div>
  <div class="social"><span></span><span></span><span></span><span></span></div>
</footer>

</body>
</html>
```